BrightHarbor logo and website profile

BrightHarbor is a newly started business angel network investing in entrepreneurs and start-ups. We need a smart looking logo and website design (based on Wordpress).
The aim of the site is to attract 2 customer segments;
1) Entrepreneurs and start-ups looking for investors
2) Investors/ business angels looking to become part of a larger network of investors for better access to investments
A successful conversion on the website would be for the entrepreneur or investor sending us an e-mail to submit their investment proposal, inquire about our services or ask to join the network of investors.
The website should focus on presenting Bright Harbor and our offerings towards the 2 customer segments. This is NOT a platform like e.g. quillfund.co.
Sites we like;
http://demo.pexorit.net/themes/marigold/agency/
http://www.tallbirchadvisory.no (it's a bit bleak - needs a little more color)
Hi all,
Reason: Been asked to extend by designers still working in their proposals.
Target Market(s)
Two target markets; 1) entrepreneurs looking for investors 2) business angels looking for investment opportunities
Industry/Entity Type
Investment
Requirements
Must have
- The keywords we want associated with our brand are;
Innovation – Integrity – Knowledgeable – Growth – Entrepreneurship
Logodesign (symbol and smart presentation of the company name - bright harbor, both with and without .com)
Wordpress design, pages we need:
- landing page with clear CTA for entrepreneurs and clear CTA for investors
- Portfolio overview of investments made
- General page for our approach, services etc
- Contact us page
- Favicon
- News
- Header/footer information
Other functionality we need;
- Social media integration
The design must support mobile and iPads as well.
We like: less is more :)

```html
<!DOCTYPE html>
<html lang="en">
<head>
<meta charset="utf-8">
<title>BrightHarbor – Business Angel Network</title>
<link rel="stylesheet" href="https://fonts.googleapis.com/css2?family=Arimo:ital,wght@0,400;0,700;1,400;1,700&family=Roboto+Condensed:ital,wght@0,400;0,700;1,400&display=swap">
<style>
:root{
  --ink:#111;
  --bar:#0b0b0b;
  --white:#fff;
  --navy:#1a3a8c;
  --green:#2a8c0c;
  --cyan:#0aa5e0;
  --footer-bg:#a9a9a9;
  --field:#c4c4c4;
  --rule:#333;
  --muted:#222;
  --brand-text:#e6e6e6;
}
*{margin:0;padding:0;box-sizing:border-box}
html,body{width:822px;height:1200px;overflow:hidden;background:var(--white)}
body{position:relative;font-family:"Arimo",Arial,sans-serif;color:var(--ink)}
.abs{position:absolute}

/* Top bar */
.topbar{left:0;top:0;width:822px;height:32px;background:var(--bar)}
.brand{left:103px;top:0;height:32px;display:flex;align-items:center;gap:6px;font-family:"Roboto Condensed",sans-serif;font-size:14px;font-weight:400;color:var(--brand-text)}
.brand-dot{width:12px;height:12px;border-radius:50%;background:var(--brand-text)}
.nav{right:102px;top:0;height:32px;display:flex;align-items:center;gap:12px;font-family:"Roboto Condensed",sans-serif;font-weight:700;font-size:8.5px;color:#e8e8e8;letter-spacing:.1px}

/* Hero */
.hero{left:0;top:32px;width:822px;height:338px;background:linear-gradient(160deg,#8e8c88 0%,#bdbab4 40%,#a29e97 70%,#6f6b66 100%)}
.hero-title{left:0;top:89px;width:822px;text-align:center;color:var(--white);font-weight:700;font-size:28.5px;line-height:35px}
.cta{width:128px;height:128px;border-radius:50%;top:177px;color:var(--white);text-align:center;font-family:"Roboto Condensed",sans-serif}
.cta-entre{left:273px;background:var(--navy)}
.cta-invest{left:421px;background:var(--green)}
.cta .lead{margin-top:33px;font-style:italic;font-size:11px;line-height:13px}
.cta .label{position:relative;display:inline-block;margin-top:8px;padding:3px 6px;font-family:"Arimo",sans-serif;font-weight:700;font-size:11.5px;line-height:14px;letter-spacing:.3px}
.cta .label::before,.cta .label::after{content:"";position:absolute;top:0;bottom:0;width:4px;border:1.2px solid var(--white)}
.cta .label::before{left:0;border-right:none}
.cta .label::after{right:0;border-left:none}
.cta .sub{margin-top:8px;font-style:italic;font-size:11px;line-height:13px}

/* Section headings */
.sec-title{left:0;width:822px;text-align:center;font-weight:700;font-size:29px}
.sec-rule{left:103px;width:616px;height:10px}

/* Projects grid */
.grid{left:103px;top:462px;width:616px;height:320px;display:grid;grid-template-columns:205px 206px 205px;grid-template-rows:160px 160px}
.tile{width:100%;height:100%}
.tile-info{background:var(--cyan);color:var(--white);text-align:center;padding:16px 13px 0}
.tile-info h3{font-size:13px;font-weight:700;padding-bottom:6px;border-bottom:1px solid rgba(255,255,255,.8);margin:0 0 9px}
.tile-info p{font-size:9px;line-height:13.5px}
.tile-info svg{margin-top:16px}

/* Clients */
.clients{left:103px;top:874px;width:616px;height:30px;display:flex;align-items:center;justify-content:space-between;font-size:13px;color:#333}
.client{display:flex;align-items:center;gap:5px;font-weight:700}
.client i{display:inline-block;width:14px;height:14px;background:#555}
.arrow{color:#888;font-size:14px;font-weight:700}

/* Footer panels */
.lower{left:0;top:942px;width:822px;height:239px;background:var(--footer-bg)}
.col-title{top:972px;width:180px;text-align:center;font-family:"Roboto Condensed",sans-serif;font-weight:700;font-size:12px;padding-bottom:5px;border-bottom:1px solid var(--rule)}
.news-img{left:103px;top:1003px;width:180px;height:64px;background:linear-gradient(100deg,#e7eef2 0%,#c9d9e0 45%,#b98463 70%,#e9e4dc 100%)}
.date{left:108px;top:1007px;width:26px;height:26px;border-radius:50%;background:#111;color:#fff;text-align:center;font-size:8px;font-weight:700;line-height:8px;padding-top:5px}
.date small{font-size:6px;font-weight:400;display:block}
.news-head{left:103px;top:1075px;font-size:10.5px;font-weight:700}
.news-text{left:103px;top:1089px;width:182px;font-size:7.5px;line-height:13.5px;color:var(--muted)}
.quote-mark{left:320px;top:993px;font-size:34px;color:#ccc;font-family:Georgia,serif;line-height:1}
.quote{left:328px;top:1011px;width:172px;font-size:7.6px;line-height:13.4px;font-style:italic;color:var(--muted)}
.quote-by{left:320px;top:1126px;width:181px;text-align:right;font-size:8.5px;font-weight:700;font-style:italic}
.t-nav{left:488px;top:974px;font-size:10px;color:#555;font-weight:700}
.field{left:539px;width:180px;background:var(--field);font-size:7.5px;padding:4px 7px;color:#111}
.send{left:662px;top:1119px;width:57px;height:29px;border-radius:5px;background:var(--cyan);color:#fff;font-weight:700;font-size:11px;display:flex;align-items:center;justify-content:center}

/* Bottom bar */
.bottom{left:0;top:1181px;width:822px;height:19px;background:var(--bar);display:flex;align-items:center;justify-content:center;gap:3px;color:#ddd;font-size:6.5px}
.bottom .sq{width:8px;height:8px;background:#bbb;display:inline-block}
.bottom span.copy{margin-right:3px}
</style>
</head>
<body>

<header class="abs topbar"></header>
<div class="abs brand"><span class="brand-dot"></span><span>BrightHarbor</span></div>
<nav class="abs nav">
  <span>ABOUT</span><span>SERVICES</span><span>PORTFOLIO</span><span>NEWS</span><span>CONTACT</span>
  <svg width="9" height="9" viewBox="0 0 9 9"><circle cx="3.6" cy="3.6" r="2.6" fill="none" stroke="#e8e8e8" stroke-width="1.4"/><line x1="5.5" y1="5.5" x2="8.3" y2="8.3" stroke="#e8e8e8" stroke-width="1.6"/></svg>
</nav>

<section class="abs hero" role="img" aria-label="Photo of a pencil resting on a page of handwritten notes"></section>
<h1 class="abs hero-title">BrightHarbor is a business angel network<br>investing in entrepreneurs &amp; start-ups</h1>

<div class="abs cta cta-entre">
  <div class="lead">I am an</div>
  <div class="label">ENTREPRENEUR</div>
  <div class="sub">looking for investors</div>
</div>
<div class="abs cta cta-invest">
  <div class="lead">I am an</div>
  <div class="label">INVESTOR</div>
  <div class="sub">looking for opportunities</div>
</div>

<h2 class="abs sec-title" style="top:400px">Featured Projects</h2>
<svg class="abs sec-rule" style="top:436px" viewBox="0 0 616 10"><path d="M0 5H300L308 11L316 5H616" fill="none" stroke="#333" stroke-width="1"/></svg>

<section class="abs grid">
  <div class="tile tile-info">
    <h3>Project Title</h3>
    <p>Lorem ipsum dolor sit amet, consectetur adipiscing elit. Curabitur sed gravida magna, blandit viverra orci. Phasellus sollicitudin mollis blandit. Cum sociis natoque penatibus et magnis parturient...</p>
    <svg width="20" height="12" viewBox="0 0 20 12"><path d="M1 6C5 0 15 0 19 6C15 12 5 12 1 6Z" fill="#fff"/><circle cx="10" cy="6" r="3" fill="var(--cyan)"/><circle cx="10" cy="6" r="1.4" fill="#fff"/></svg>
  </div>
  <div class="tile" role="img" aria-label="Restaurant interior with round bar and hanging lamps" style="background:linear-gradient(160deg,#3a2a1a,#b5732e 45%,#6f6a2a 75%,#2c2016)"></div>
  <div class="tile" role="img" aria-label="Skateboarder in mid-air against a blue sky" style="background:linear-gradient(170deg,#2f3f8e,#5a79c4 55%,#6f8a5a 85%,#3a3a3a)"></div>
  <div class="tile" role="img" aria-label="Fashion shoot with a group of models" style="background:linear-gradient(150deg,#5a1010,#9e2020 45%,#2a1a1a 75%,#8a8580)"></div>
  <div class="tile" role="img" aria-label="Community project with children planting a tree" style="background:linear-gradient(180deg,#b6b6b0,#8a6a4a 40%,#6e5a3a 75%,#5a4a2a)"></div>
  <div class="tile" role="img" aria-label="Colourful mural artwork" style="background:linear-gradient(140deg,#2a6fa8,#d45a2a 40%,#e0b030 65%,#3a8a6a)"></div>
</section>

<h2 class="abs sec-title" style="top:813px">Clients</h2>
<svg class="abs sec-rule" style="top:849px" viewBox="0 0 616 10"><path d="M0 5H300L308 11L316 5H616" fill="none" stroke="#333" stroke-width="1"/></svg>

<div class="abs clients">
  <span class="arrow">&#8249;</span>
  <span class="client"><i></i>Northwind</span>
  <span class="client">Fizzbay</span>
  <span class="client"><i></i>Tangerio</span>
  <span class="client">Speedloop</span>
  <span class="client">Corvana</span>
  <span class="client">The Daily Ledger</span>
  <span class="arrow">&#8250;</span>
</div>

<section class="abs lower"></section>

<h3 class="abs col-title" style="left:103px">LATEST NEWS</h3>
<h3 class="abs col-title" style="left:321px">TESTIMONIALS</h3>
<h3 class="abs col-title" style="left:539px">QUICK INQUIRY</h3>

<div class="abs news-img" role="img" aria-label="Surfer carrying a board along the beach"></div>
<div class="abs date">18<small>Jun</small></div>
<div class="abs news-head">Lorem ipsum dolor sit amet</div>
<p class="abs news-text">Lorem ipsum dolor sit amet, consectetur adipiscing elit. Ut et massa id urna gravida dignissim. Morbi dapibus sit amet augue quis pharetra. Maecenas nibh urna, fac ilisis in hen sura drerit tincid vida digniunt, faucibus...</p>

<div class="abs t-nav">&#8249; &#8250;</div>
<div class="abs quote-mark">&ldquo;</div>
<p class="abs quote">Lorem ipsum dolor sit amet, consectetur adipiscing elit. Ut et massa id urna gravida dignissim. Morbi dapibus sit amet augue quis pharetra. Maecenas nibh urna, facilisis in hendrerit tincidunt, faucibus quis augue. Nulla ante nunc, luctus quis nisi eu, fermentum elementum metus. Ut semper sollicitudin lorem ac aliquam. Nam semper turpis mauris, ut fringilla neque tempus quis amet.</p>
<div class="abs quote-by">- Daniel Ostrow, Kestrel Goods</div>

<div class="abs field" style="top:1003px;height:19px">Name</div>
<div class="abs field" style="top:1026px;height:19px">Email</div>
<div class="abs field" style="top:1049px;height:63px">Message</div>
<div class="abs send">
  <svg width="40" height="18" viewBox="0 0 40 18" style="position:absolute"><path d="M4 1H1V17H4M36 1H39V17H36" fill="none" stroke="#fff" stroke-width="1.1"/></svg>SEND
</div>

<footer class="abs bottom">
  <span class="copy">©2013 BrightHarbor.</span>
  <i class="sq"></i><i class="sq"></i><i class="sq"></i><i class="sq"></i><i class="sq"></i>
</footer>

</body>
</html>
```